Unique Hair Product needs upscale Tube Design

Velandra's Henna is a hair product company. I need a tube design for a 4oz ABL (soft aluminum) tube which incorporates my logo and product information and usage. The product is a high-end treatment for thicker, darker hair.

Velandra's Henna is a unique, strengthening color treatment, that will thicken weak, damaged hair, while enhancing hair color naturally, with henna.

Target Market(s)

Women age 17 and up

Industry/Entity Type

Hair Care Product

Requirements
Must have
• "Strengthening, Color enhancing, Hair treatment" this product description must be on the front of the tube. Please use diagram below.
• Must have logo placed strategically, and placed beautifully. I need the tube design to be elegant and beautiful because it is a high end product. Please use colors that you think would look nice and appeal to women. I was thinking a nice light olive green, with a white logo, but play with it until it looks really pretty.
• It will be going into a box, similar to the one below.
Nice to have
• Elegance, clarity and sharp
• please use the diagram to properly place the design in the designated space below
Should not have
• Please no cursive writing

```html
<!DOCTYPE html>
<html lang="en">
<head>
<meta charset="utf-8">
<title>Velandra's Henna – Tube Label</title>
<link rel="stylesheet" href="https://fonts.googleapis.com/css2?family=Alegreya+Sans+SC:wght@700&family=Cinzel:wght@500;600&family=Raleway:wght@300;400&family=Oswald:wght@500&display=swap">
<style>
  :root {
    --page: #ffffff;
    --plum: #5e3649;
    --blush: #e0c3cf;
    --blush-text: #f0d9e2;
    --plum-soft: #6c4357;
    --blush-deep: #d5b1c1;
    --ink: #5b3a4a;
  }
  * { margin: 0; padding: 0; box-sizing: border-box; }
  html, body { width: 1200px; height: 1000px; overflow: hidden; background: var(--page); }
  .canvas { position: relative; width: 1200px; height: 1000px; }

  .label { position: absolute; left: 282px; top: 141px; width: 636px; height: 718px; display: flex; }

  .front { position: relative; width: 318px; height: 100%; background: var(--plum); color: var(--blush-text); text-align: center; }
  .back { position: relative; width: 318px; height: 100%; background: var(--blush); color: var(--ink); }

  .brand { position: absolute; top: 82px; left: 0; width: 100%; display: flex; flex-direction: column; align-items: center; gap: 10px; }
  .brand-dot { width: 34px; height: 34px; border-radius: 50%; border: 2px solid var(--blush-text); }
  .brand-name { font-family: "Cinzel", serif; font-weight: 500; font-size: 16px; letter-spacing: 0.5px; color: var(--blush-text); }

  .front-title { position: absolute; top: 204px; left: 0; width: 100%; font-family: "Alegreya Sans SC", sans-serif; font-weight: 700; font-size: 41px; line-height: 60px; color: var(--blush-text); }

  .flourish { position: absolute; left: 126px; width: 66px; height: 10px; }
  .flourish-top { top: 404px; }
  .flourish-bottom { top: 656px; }

  .front-copy { position: absolute; top: 443px; left: 0; width: 100%; font-family: "Raleway", sans-serif; font-weight: 300; font-size: 19px; line-height: 27px; color: var(--blush-text); }

  .front-ornament { position: absolute; left: 40px; top: 560px; width: 238px; height: 158px; background: radial-gradient(ellipse at 50% 60%, var(--plum-soft), rgba(94,54,73,0) 70%); }

  .back-title { position: absolute; top: 94px; left: 0; width: 100%; text-align: center; font-family: "Cinzel", serif; font-weight: 600; font-size: 22px; line-height: 28px; letter-spacing: 1px; color: var(--ink); }

  .back-ornament { position: absolute; left: 0; top: 40px; width: 318px; height: 270px; background: radial-gradient(ellipse at 85% 55%, var(--blush-deep), rgba(224,195,207,0) 65%); }

  .ingredients { position: absolute; top: 345px; left: 31px; list-style: none; font-family: "Raleway", sans-serif; font-weight: 400; font-size: 13.5px; line-height: 27px; color: var(--ink); }

  .net-weight { position: absolute; right: 25px; top: 670px; font-family: "Oswald", sans-serif; font-weight: 500; font-size: 22px; color: var(--ink); }
</style>
</head>
<body>
<div class="canvas">
  <div class="label">
    <section class="front">
      <div class="front-ornament" role="img" aria-label="Faint decorative scrollwork"></div>
      <div class="brand">
        <span class="brand-dot"></span>
        <span class="brand-name">VELANDRA'S HENNA</span>
      </div>
      <h1 class="front-title">Strengthening<br>Color Enhancing<br>Hair Treatment</h1>
      <svg class="flourish flourish-top" viewBox="0 0 66 10"><path d="M1 5 Q17 9 33 5 Q49 1 65 5" fill="none" stroke="var(--blush-text)" stroke-width="2"/></svg>
      <p class="front-copy">Velandra's Henna is a unique,<br>strengthening color treatment,<br>that will thicken weak,<br>damaged hair,<br>while enhancing hair<br>color naturally,<br>with henna.</p>
      <svg class="flourish flourish-bottom" viewBox="0 0 66 10"><path d="M16 5 Q24 8 33 5 Q42 2 50 5" fill="none" stroke="var(--plum-soft)" stroke-width="2"/></svg>
    </section>
    <section class="back">
      <div class="back-ornament" role="img" aria-label="Faint decorative scrollwork"></div>
      <h2 class="back-title">STRENGTHENING<br>COLOR ENHANCING<br>HAIR TREATMENT</h2>
      <ul class="ingredients">
        <li>Ingredients:</li>
        <li>Lorem ipsum dolor sit amet,</li>
        <li>consectetuer adipiscing elit.</li>
        <li>In rutrum. Integer in sapien.</li>
        <li>Fusce dui leo, imperdiet in,</li>
        <li>aliquam sit amet, feugiat eu, orci.</li>
        <li>Nullam eget nisl. Aliquam erat volutpat.</li>
        <li>Proin pede metus, vulputate nec,</li>
        <li>fermentum fringilla, vehicula vitae,</li>
        <li>justo. Vivamus ac leo pretium faucibus.</li>
        <li>Nullam rhoncus aliquam metus.</li>
        <li>Proin mattis lacinia justo.</li>
      </ul>
      <p class="net-weight">Netto:120g</p>
    </section>
  </div>
</div>
</body>
</html>
```